bluecastle aquatics of northeast florida business card

I need a new attractive business card. I am planning on printing on very thick rounded corner stock and having painted edges. We are a swimming pool remodel, repair, and service company in north florida. Our current logo is red, white, and blue. It doesn't necessarily have to stay that way, I am open to other ideas. It will need to contain my name, work and cell numbers, email, website, and my contractor license number.

Target Market(s)

High end residential and commercial clients

Industry/Entity Type

Business

Contact Information for Business Card

Company name, employee name and title, work and cell phone numbers, email and website, and Contractor number.

our work scope should be on card somewhere: remodel ~ repair ~ service

logo or slight variation of logo also. (not necessarily set on keeping exact logo)

Colors

Designer to choose colors to be used in the design.

Requirements
Nice to have
• We deal with water so I think some sort of water element or just a color similar to pool water would be nice to integrate into design.

```html
<!DOCTYPE html>
<html lang="en">
<head>
<meta charset="utf-8">
<title>Bluecastle Aquatics – Business Card</title>
<link rel="stylesheet" href="https://fonts.googleapis.com/css2?family=Libre+Baskerville:wght@400;700&family=Arimo:wght@400&display=swap">
<style>
  :root {
    --bg: #2b2b2b;
    --paper: #ffffff;
    --brand-blue: #1f6fb5;
    --deep-blue: #1d4f86;
    --brand-red: #e2262b;
    --faint-blue: #dde4f1;
    --ink: #222a3a;
  }
  * { margin: 0; padding: 0; box-sizing: border-box; }
  html, body { width: 1200px; height: 852px; overflow: hidden; background: var(--bg); }
  .stage { position: relative; width: 1200px; height: 852px; }
  .card {
    position: absolute; width: 540px; height: 310px;
    background: var(--paper); border-radius: 22px; overflow: hidden;
    box-shadow: 0 12px 30px rgba(0,0,0,.45);
  }
  .card--front { left: 50px; top: 120px; }
  .card--back { left: 610px; top: 420px; }
  .card__waves { position: absolute; inset: 0; width: 100%; height: 100%; }
  .brand { position: absolute; display: flex; align-items: center; gap: 10px; }
  .brand__dot { width: 30px; height: 30px; border-radius: 50%; background: var(--brand-blue); flex: none; }
  .brand__name {
    font-family: "Libre Baskerville", serif; font-weight: 700; color: var(--brand-blue);
    line-height: 1.15; text-transform: uppercase;
  }
  .brand__main { display: block; font-size: 19px; letter-spacing: 2px; }
  .brand__sub { display: block; font-size: 10.5px; letter-spacing: 2.3px; border-top: 1px solid var(--brand-blue); padding-top: 2px; }
  .card--front .brand { left: 105px; top: 108px; }
  .card--back .brand { left: 30px; top: 62px; }
  .scope {
    position: absolute; left: 205px; top: 272px;
    font-family: "Libre Baskerville", serif; font-size: 13px; color: var(--paper);
    white-space: nowrap;
  }
  .faint-circle {
    position: absolute; right: -40px; top: -80px; width: 250px; height: 250px;
    border-radius: 50%; background: var(--faint-blue);
  }
  .divider { position: absolute; left: 30px; top: 142px; width: 470px; height: 1px; background: var(--deep-blue); }
  .person { position: absolute; left: 30px; top: 152px; font-family: "Libre Baskerville", serif; }
  .person__name { font-size: 18px; font-weight: 700; color: var(--deep-blue); }
  .person__title { font-size: 12px; color: var(--brand-blue); margin-top: 2px; }
  .contact { font-family: "Arimo", sans-serif; font-size: 14px; color: var(--ink); }
  .phones { position: absolute; left: 30px; top: 200px; display: grid; gap: 4px; }
  .online { position: absolute; right: 24px; top: 98px; display: grid; gap: 4px; text-align: right; font-size: 12.5px; }
  .row { display: flex; align-items: center; gap: 7px; }
  .online .row { justify-content: flex-end; }
  .icon { width: 13px; height: 13px; flex: none; fill: var(--brand-red); }
  .licence {
    position: absolute; right: 28px; top: 250px;
    font-family: "Arimo", sans-serif; font-size: 12.5px; color: var(--paper);
  }
</style>
</head>
<body>
<main class="stage">

  <section class="card card--front" aria-label="Card front">
    <svg class="card__waves" viewBox="0 0 540 310" aria-hidden="true">
      <path fill="var(--brand-blue)" d="M0 200 C150 178 330 262 540 120 L540 130 C330 272 150 188 0 210 Z"/>
      <path fill="var(--brand-red)" d="M0 218 C150 196 330 280 540 140 L540 152 C330 292 150 210 0 230 Z"/>
      <path fill="var(--brand-blue)" d="M0 240 C150 218 330 300 540 165 L540 310 L0 310 Z"/>
    </svg>
    <div class="brand">
      <span class="brand__dot"></span>
      <span class="brand__name"><span class="brand__main">Bluecastle Aquatics</span><span class="brand__sub">of Northeast Florida</span></span>
    </div>
    <p class="scope">Remodel ~ Repair ~ Service</p>
  </section>

  <section class="card card--back" aria-label="Card back">
    <div class="faint-circle"></div>
    <svg class="card__waves" viewBox="0 0 540 310" aria-hidden="true">
      <path fill="var(--brand-blue)" d="M0 262 C160 250 330 250 540 178 L540 186 C330 260 160 262 0 270 Z"/>
      <path fill="var(--brand-red)" d="M0 276 C160 262 330 262 540 196 L540 208 C330 276 160 278 0 288 Z"/>
      <path fill="var(--brand-blue)" d="M0 296 C170 282 330 290 540 222 L540 310 L0 310 Z"/>
    </svg>
    <div class="brand">
      <span class="brand__dot"></span>
      <span class="brand__name"><span class="brand__main">Bluecastle Aquatics</span><span class="brand__sub">of Northeast Florida</span></span>
    </div>
    <div class="divider"></div>
    <div class="person">
      <p class="person__name">Daniel Whitford</p>
      <p class="person__title">Managing Director</p>
    </div>
    <div class="phones contact">
      <p class="row"><svg class="icon" viewBox="0 0 16 16"><path d="M3 1l3 3-2 2c1 2 3 4 5 5l2-2 3 3-2 3C6 14 2 10 1 3z"/></svg>904.555.0137</p>
      <p class="row"><svg class="icon" viewBox="0 0 16 16"><path d="M4 1h8v4H4zM1 6h14v6h-3v3H4v-3H1zM5 10v4h6v-4z"/></svg>904.555.0182</p>
    </div>
    <div class="online contact">
      <p class="row">hello@bluecastleaquatics.com<svg class="icon" viewBox="0 0 16 16"><path d="M1 3h14v10H1zM2 4l6 5 6-5v-.5H2z"/></svg></p>
      <p class="row">www.bluecastleaquatics.com<svg class="icon" viewBox="0 0 16 16"><circle cx="8" cy="8" r="7"/></svg></p>
    </div>
    <p class="licence">Lic No : 0481927</p>
  </section>

</main>
</body>
</html>
```